I have a basketball training business combined with a strength training business. I train professio

I recently saw the cats that won the contest in the strength coach business card competition. I loved the design. I.want a card with my logo that calls attention to my clients as the card that won did to me. I would like to see if I could get a similar design. My logo is what I like although I must say I like the red and black design of the contest winner. perhaps if the smaller lettered portion of my logo coukd be separated from the larger KQT logo. It almost looks like 3M3. I like.the KQT Training and Development portion of it. I need help.

Training

```html
<!DOCTYPE html>
<html lang="en">
<head>
<meta charset="utf-8">
<title>KQT Training and Development – Business Card</title>
<link rel="stylesheet" href="https://fonts.googleapis.com/css2?family=Roboto:wght@300;400;700&display=swap">
<style>
  :root {
    --bg: #e9e7e4;
    --card-white: #ffffff;
    --card-red: #ec412c;
    --ink-dark: #3a3a3a;
    --ink-black: #111111;
    --icon-bg: #0d0d0d;
    --icon-fg: #ffffff;
  }
  * { margin: 0; padding: 0; box-sizing: border-box; }
  html, body {
    width: 1200px; height: 848px; overflow: hidden;
    background: var(--bg);
    font-family: "Roboto", Arial, sans-serif;
  }
  .canvas {
    position: relative; width: 1200px; height: 848px;
    display: flex; align-items: center; justify-content: center;
  }
  .card {
    position: relative; width: 1000px; height: 572px;
    border-radius: 34px; overflow: hidden;
    background: var(--card-red);
    box-shadow: 0 14px 40px rgba(0,0,0,0.18);
  }
  .card__top {
    position: absolute; left: 0; top: 0; right: 0; height: 190px;
    background: var(--card-white);
  }
  .brand {
    position: absolute; left: 400px; top: 42px;
    display: flex; align-items: center; gap: 18px;
    color: var(--ink-dark); font-weight: 700;
  }
  .brand__mark {
    width: 70px; height: 70px; background: var(--ink-dark);
  }
  .brand__name { display: flex; flex-direction: column; line-height: 1; }
  .brand__initials { font-size: 64px; letter-spacing: -1px; }
  .brand__tagline { font-size: 21px; letter-spacing: 2px; text-transform: uppercase; margin-top: 6px; }
  .person {
    position: absolute; left: 0; right: 0; top: 218px;
    text-align: center; color: var(--ink-black);
  }
  .person__name { font-size: 44px; font-weight: 300; }
  .person__cred { font-size: 24px; font-weight: 300; margin-top: 6px; }
  .person__cert { font-size: 24px; font-weight: 300; margin-top: 4px; }
  .contact {
    position: absolute; bottom: 58px;
    display: flex; align-items: center; gap: 22px;
    color: var(--ink-black); font-size: 27px; font-weight: 300;
  }
  .contact--phone { left: 54px; }
  .contact--web { right: 56px; }
  .contact__icon {
    width: 40px; height: 40px; background: var(--icon-bg);
    display: flex; align-items: center; justify-content: center;
  }
</style>
</head>
<body>
<main class="canvas">
  <article class="card">
    <div class="card__top"></div>

    <div class="brand">
      <div class="brand__mark"></div>
      <div class="brand__name">
        <span class="brand__initials">KQT</span>
        <span class="brand__tagline">Training and Development</span>
      </div>
    </div>

    <section class="person">
      <h1 class="person__name">Jordan Hale</h1>
      <p class="person__cred">NSTA C-PT,CES</p>
      <p class="person__cert">CSTC (Certified Strength Training Coach)</p>
    </section>

    <div class="contact contact--phone">
      <span class="contact__icon">
        <svg width="26" height="26" viewBox="0 0 24 24" aria-hidden="true">
          <path fill="var(--icon-fg)" d="M6.6 10.8c1.4 2.8 3.8 5.1 6.6 6.6l2.2-2.2c.3-.3.7-.4 1-.2 1.1.4 2.3.6 3.6.6.6 0 1 .4 1 1V20c0 .6-.4 1-1 1C10.6 21 3 13.4 3 4c0-.6.4-1 1-1h3.5c.6 0 1 .4 1 1 0 1.3.2 2.5.6 3.6.1.3 0 .7-.2 1l-2.3 2.2z"/>
        </svg>
      </span>
      <span class="contact__text">555 010 0199</span>
    </div>

    <div class="contact contact--web">
      <span class="contact__icon">
        <svg width="26" height="26" viewBox="0 0 24 24" aria-hidden="true" fill="none" stroke="var(--icon-fg)" stroke-width="1.8">
          <circle cx="12" cy="12" r="9"/>
          <ellipse cx="12" cy="12" rx="4" ry="9"/>
          <line x1="3" y1="12" x2="21" y2="12"/>
        </svg>
      </span>
      <span class="contact__text">Www.jordanhalebasketball.com</span>
    </div>
  </article>
</main>
</body>
</html>
```